2 Wine Label Designs

Amberly Cellars has been helping people give customized wine gifts since 1999. From large scale corporate clients, to 1 bottle personalized gifts, we offer a wide range of wines and templates for any occasion. Recently we’ve started to shift our focus to a younger demographic (21 to 35 year old women) and are in the process of updating our website and branding.

One big area we’re working to improve is the customizable wine label/engraving templates we offer on the site (to see our current template library go to www.amberlycellars.com/shop/wine, select a wine, choose “label” or “engraving” from the dropdown, and click “customize”). You’ll find that a lot of our current templates are outdated or aimed at an older demographic. Over the next few months we want to swap out most of these old templates with fun fresh designs.

We're asking designers to submit 2 customizable wine label templates for this project. One should be wedding themed and the other "Thank You" themed. Please see the attached PDF for more guidelines and creative direction.

Keep in mind, even if you aren't selected as the winner of this project we are going to go through and offer $50 for any label template submitted that we like ($100 if we want both). So there is a good chance you'll be getting some money for your work!

Please read though the attached guidelines PDF carefully (especially the "Must be Customizable" section).

Target Market(s)

21 to 35 year old women

Colors

Designer to choose colors to be used in the design.

Requirements
Must have
• See attached PDF
Nice to have
• See attached PDF
Should not have
• See attached PDF

```html
<!DOCTYPE html>
<html lang="en">
<head>
<meta charset="utf-8">
<title>Amberly Cellars – Thank You &amp; Wedding Labels</title>
<link rel="stylesheet" href="https://fonts.googleapis.com/css2?family=Josefin+Sans:wght@300;400&family=Great+Vibes&family=Allura&family=Cinzel:wght@400&family=Playfair+Display:wght@400&display=swap">
<style>
  :root {
    --backdrop: #e3e2da;
    --label-cream: #f1ecd8;
    --cream-line: #b9a877;
    --wine-red: #c8102e;
    --band-red: #a3242c;
    --gold: #e0a43a;
    --ink: #1a1a1a;
    --white: #f4f4f4;
  }
  * { box-sizing: border-box; margin: 0; padding: 0; }
  html, body { width: 1146px; height: 1200px; overflow: hidden; }
  body {
    background: var(--backdrop);
    position: relative;
    font-family: "Josefin Sans", sans-serif;
  }

  /* ---------- Thank You label ---------- */
  .label-thanks {
    position: absolute;
    left: 60px; top: 330px;
    width: 500px; height: 540px;
    background: repeating-linear-gradient(60deg, #181818 0 2px, #121212 2px 5px);
    color: var(--white);
    text-align: center;
    overflow: hidden;
  }
  .label-thanks .brand {
    position: absolute; top: 62px; left: 0; right: 0;
    display: flex; justify-content: center; align-items: center; gap: 12px;
    font-weight: 300; font-size: 24px; letter-spacing: 3px; color: var(--white);
  }
  .brand-dot { width: 11px; height: 11px; border-radius: 50%; background: var(--wine-red); flex: none; }
  .label-thanks .headline {
    position: absolute; top: 112px; left: 0; right: 0;
    font-family: "Great Vibes", cursive;
    font-weight: 400;
    line-height: 0.95;
  }
  .headline .word-thank {
    display: block; font-size: 128px;
    background: linear-gradient(90deg, #f0a020, #f4d04a 30%, #e8386a 65%, #f6a6d8);
    -webkit-background-clip: text; background-clip: text; color: transparent;
  }
  .headline .word-you {
    display: block; font-size: 112px; margin-top: -14px; padding-left: 30px;
    background: linear-gradient(90deg, #e0205a, #c81e4a 60%, #e85090);
    -webkit-background-clip: text; background-clip: text; color: transparent;
  }
  .label-thanks .recipient-frame {
    position: absolute; top: 412px; left: 150px; width: 200px; height: 62px;
    border-top: 2px solid #cfcfcf; border-bottom: 2px solid #cfcfcf;
  }
  .label-thanks .recipient {
    position: absolute; top: 418px; left: 0; right: 0;
    font-family: "Allura", cursive; font-size: 40px; line-height: 1; color: var(--wine-red);
  }
  .label-thanks .message {
    position: absolute; top: 494px; left: 0; right: 0;
    font-size: 16px; letter-spacing: 1.5px; color: var(--gold); font-weight: 300;
  }

  /* ---------- Wedding label ---------- */
  .label-wedding {
    position: absolute;
    left: 620px; top: 150px;
    width: 450px; height: 900px;
    background: var(--label-cream);
    text-align: center;
    color: var(--ink);
    overflow: hidden;
  }
  .label-wedding .rule { position: absolute; left: 0; right: 0; height: 2px; background: var(--cream-line); }
  .rule.top-1 { top: 22px; }
  .rule.top-2 { top: 36px; }
  .label-wedding .brand {
    position: absolute; top: 228px; left: 0; right: 0;
    display: flex; justify-content: center; align-items: center; gap: 12px;
    font-weight: 400; font-size: 28px; letter-spacing: 2px; color: var(--ink);
  }
  .label-wedding .title {
    position: absolute; top: 290px; left: 0; right: 0;
    font-family: "Great Vibes", cursive; font-weight: 400;
    font-size: 112px; line-height: 1;
    color: var(--ink);
  }
  .title .initial { color: var(--wine-red); }
  .label-wedding .rings {
    position: absolute; top: 478px; left: 197px; width: 56px; height: 34px;
    border-radius: 17px; background: linear-gradient(90deg, #d0252e, #a81e28);
  }
  .label-wedding .couple {
    position: absolute; top: 526px; left: 0; right: 0;
    font-family: "Cinzel", serif; font-size: 56px; line-height: 1.1; color: var(--wine-red); letter-spacing: 1px;
  }
  .label-wedding .toast {
    position: absolute; top: 614px; left: 0; right: 0;
    display: flex; justify-content: center; align-items: center; gap: 14px;
    font-size: 20px; letter-spacing: 1.5px; font-weight: 300;
  }
  .toast .accent { color: var(--wine-red); }
  .toast .spark { width: 20px; height: 20px; border-radius: 50%; background: #7a7a7a; opacity: 0.6; }
  .label-wedding .band-rule { position: absolute; left: 0; right: 0; height: 2px; background: var(--cream-line); }
  .band-rule.upper { top: 684px; }
  .band-rule.lower { top: 830px; }
  .label-wedding .vintage-band {
    position: absolute; top: 694px; left: 0; right: 0; height: 128px;
    background: var(--band-red);
  }
  .vintage-band .year {
    position: absolute; top: 26px; left: 0; right: 0;
    font-family: "Playfair Display", serif; font-size: 60px; color: var(--gold); line-height: 1;
  }
  .vintage-band .volume {
    position: absolute; top: 96px; left: 0; right: 0;
    font-size: 13px; letter-spacing: 1px; color: var(--white);
  }
  .vintage-band .wreath {
    position: absolute; top: 24px; width: 60px; height: 84px; border-radius: 30px;
    background: linear-gradient(180deg, rgba(240,220,210,0.35), rgba(240,220,210,0.15));
  }
  .wreath.left { left: 90px; }
  .wreath.right { right: 90px; }
</style>
</head>
<body>

  <section class="label-thanks" aria-label="Thank You wine label">
    <div class="brand"><span class="brand-dot"></span>AMBERLY CELLARS</div>
    <h1 class="headline"><span class="word-thank">Thank</span><span class="word-you">You</span></h1>
    <div class="recipient-frame"></div>
    <p class="recipient">Rosalind</p>
    <p class="message">THANKS FOR ALL YOUR HELP</p>
  </section>

  <section class="label-wedding" aria-label="Wedding wine label">
    <div class="rule top-1"></div>
    <div class="rule top-2"></div>
    <div class="brand"><span class="brand-dot"></span>AMBERLY CELLARS</div>
    <h1 class="title"><span class="initial">W</span>edding</h1>
    <div class="rings" role="img" aria-label="Interlocking wedding rings ornament"></div>
    <p class="couple">MR &amp; MRS.</p>
    <p class="toast">
      <span class="spark" role="img" aria-label="Sparkle ornament"></span>
      <span>A TOAST TO <span class="accent">LOVE</span></span>
      <span class="spark" role="img" aria-label="Sparkle ornament"></span>
    </p>
    <div class="band-rule upper"></div>
    <div class="vintage-band">
      <div class="wreath left" role="img" aria-label="Laurel branch ornament"></div>
      <p class="year">2018</p>
      <p class="volume">750ML</p>
      <div class="wreath right" role="img" aria-label="Laurel branch ornament"></div>
    </div>
    <div class="band-rule lower"></div>
  </section>

</body>
</html>
```